Pricing sheet For Acupuncture Clinic - Remake Attached Work

Right Now I have 4 pricing sheets that look very disorganized. They are for 4 different options of services I offer with 3 different options to pay for each service (pay each time you come in, prepaid package, or a monthly option). People get confused from this outline so looking to make this easier to understand and better looking. You can reorganize the pricing as you see fit as long as it makes sense. (ex: using columns or rows or a graph) These images are going to be made into standard sized posters (i think that is 5 feet by 7 feet?)

Instead of designing all 4 of the attached files below you can choose 1 of them to show your example of work. I will assume that style will apply to all 4 sheets if I choose your work - also need 1 sheet that can print out on paper that will show all treatments on front and back of paper.

Thank you
Milo

Target Market(s)

Spa Industry

Industry/Entity Type

Clinic

Font styles to use
Serif
Sans Serif
Decorative
Script

Colors
33a6d7
ffffff
000000

Requirements
Nice to have
• clean - organized -
Should not have
• pictures of acupuncture needles. anything sharp. anything that might make people feel afraid of getting the treatments or look painful

```html
<!DOCTYPE html>
<html lang="en">
<head>
<meta charset="utf-8">
<title>Harbor Glow Acupuncture – Micro-Needling Pricing</title>
<link rel="stylesheet" href="https://fonts.googleapis.com/css2?family=Bebas+Neue&family=Open+Sans:wght@400;600;700&display=swap">
<style>
  :root {
    --artboard: #5c5e5d;
    --aqua: #33c3d9;
    --aqua-deep: #33a6d7;
    --ink: #000000;
    --paper: #ffffff;
    --panel-dark: #1c1c1c;
    --panel-mid: #3a3a3a;
    --text-dark: #1a1a1a;
  }
  * { box-sizing: border-box; margin: 0; padding: 0; }
  html, body { width: 997px; height: 1200px; overflow: hidden; }
  body {
    background: var(--artboard);
    font-family: "Open Sans", Arial, sans-serif;
    position: relative;
  }
  .pricing-sheet {
    position: absolute;
    left: 110px; top: 96px;
    width: 725px; height: 1007px;
    background: var(--paper);
    overflow: hidden;
  }
  .hero-photo {
    position: absolute; left: 0; top: 0;
    width: 725px; height: 392px;
    background:
      radial-gradient(ellipse 55% 70% at 70% 55%, #f1d3c6 0%, #e6c0b2 45%, rgba(230,200,190,0) 75%),
      linear-gradient(100deg, #e9edf0 0%, #dfe3e6 30%, #efe2dc 60%, #d9d9db 100%);
  }
  .hero-divider {
    position: absolute; left: 0; top: 392px;
    width: 725px; height: 12px;
    background: linear-gradient(to bottom, #d7d2d2, #bfb8b8);
  }
  .brand-mark {
    position: absolute; left: 38px; top: 34px;
    width: 175px; height: 143px;
    background: var(--paper);
    display: flex; align-items: center; justify-content: center;
    text-align: center;
    font-family: "Bebas Neue", Impact, sans-serif;
    color: var(--aqua-deep);
    font-size: 31px; line-height: 28px;
    letter-spacing: 1px;
  }
  .price-panel {
    position: absolute; left: 0; top: 404px;
    width: 725px; height: 441px;
    background: radial-gradient(ellipse 60% 55% at 50% 35%, var(--panel-mid) 0%, var(--panel-dark) 80%);
    color: var(--paper);
  }
  .service-title {
    position: absolute; left: 0; top: 20px; width: 100%;
    text-align: center; white-space: nowrap;
    font-family: "Bebas Neue", Impact, sans-serif;
    font-size: 60px; line-height: 64px;
    color: var(--aqua);
    letter-spacing: 0.5px;
  }
  .service-subtitle {
    position: absolute; left: 0; top: 104px; width: 100%;
    text-align: center;
    font-size: 23px; font-weight: 400;
  }
  .plan-card {
    position: absolute; top: 174px;
    width: 214px; height: 240px;
    border: 3px dotted var(--paper);
    border-radius: 10px;
    text-align: center;
  }
  .plan-card.pay-as-you-go { left: 23px; }
  .plan-card.prepaid { left: 256px; }
  .plan-card.autopay { left: 489px; }
  .plan-name {
    margin-top: 20px;
    font-family: "Bebas Neue", Impact, sans-serif;
    font-size: 31px; line-height: 34px;
    color: var(--aqua);
  }
  .plan-rule {
    width: 176px; height: 2px; margin: 8px auto 0;
    background: var(--paper);
  }
  .plan-note { margin-top: 6px; font-size: 13px; }
  .plan-tier { font-size: 19px; line-height: 21px; }
  .plan-price { font-size: 19px; line-height: 21px; font-weight: 700; color: var(--aqua); margin-bottom: 2px; }
  .retail { margin-top: 38px; font-size: 19px; line-height: 22px; }
  .our-price { margin-top: 10px; font-size: 19px; line-height: 22px; font-weight: 600; color: var(--aqua); }
  .terms {
    position: absolute; left: 0; top: 845px;
    width: 725px; height: 88px;
    padding-top: 8px;
    text-align: center;
    font-size: 11.5px; line-height: 18px;
    color: var(--text-dark);
    text-transform: uppercase;
  }
  .contact-bar {
    position: absolute; left: 0; top: 933px;
    width: 725px; height: 74px;
    background: var(--aqua);
    color: var(--paper);
    display: flex; align-items: center; justify-content: center;
    gap: 28px;
    font-size: 12.5px;
  }
  .contact-item { display: flex; align-items: center; gap: 6px; white-space: nowrap; }
  .contact-item svg { width: 14px; height: 14px; }
</style>
</head>
<body>
  <main class="pricing-sheet">
    <div class="hero-photo" role="img" aria-label="Close-up photo of a woman receiving a gentle facial skin treatment"></div>
    <div class="hero-divider"></div>
    <div class="brand-mark">Harbor Glow<br>Acupuncture</div>

    <section class="price-panel">
      <h1 class="service-title">Micro - Needling / Nano - Needling</h1>
      <p class="service-subtitle">(With apple Stem Cells)</p>

      <div class="plan-card pay-as-you-go">
        <h2 class="plan-name">Pay As You Go</h2>
        <div class="plan-rule"></div>
        <p class="retail">Retail: $800<br>Treatment</p>
        <p class="our-price">Our price: $400<br><span style="font-weight:400">Treatment</span></p>
      </div>

      <div class="plan-card prepaid">
        <h2 class="plan-name">Pre-Paid Packages</h2>
        <div class="plan-rule"></div>
        <p class="plan-note">Use Anytime For 1 Year</p>
        <p class="plan-tier">6 Treatments/month</p>
        <p class="plan-price">$1100/month</p>
        <p class="plan-tier">12 Treatments/Month</p>
        <p class="plan-price">$2000/month</p>
        <p class="plan-tier">24 Treatments/Month</p>
        <p class="plan-price">$3600/month</p>
      </div>

      <div class="plan-card autopay">
        <h2 class="plan-name">Monthly Autopay</h2>
        <div class="plan-rule"></div>
        <p class="plan-note">Roll Over - Min 4 Months</p>
        <p class="plan-tier">4 Treatments/month</p>
        <p class="plan-price">$230/month</p>
        <p class="plan-tier">8 Treatments/Month</p>
        <p class="plan-price">$400/month</p>
        <p class="plan-tier">12 Treatments/Month</p>
        <p class="plan-price">$800/month</p>
      </div>
    </section>

    <section class="terms">
      <p>Auto pay unused treatments roll - over - pre-paid package expire af ter 1 year</p>
      <p>Autopay may be cancelled anytime after 4 months</p>
      <p>Monthly autopay unused treatments</p>
      <p>Will be forfeited 3 months after cancellation</p>
    </section>

    <footer class="contact-bar">
      <span class="contact-item">
        <svg viewBox="0 0 14 14"><path d="M7 0.5a4.5 4.5 0 0 0-4.5 4.5c0 3.4 4.5 8.5 4.5 8.5s4.5-5.1 4.5-8.5A4.5 4.5 0 0 0 7 .5z" fill="#fff"/><circle cx="7" cy="5" r="1.7" fill="#33c3d9"/></svg>
        2217 Seabright Avenue, Coral Bay, CA 90210
      </span>
      <span class="contact-item">
        <svg viewBox="0 0 14 14"><circle cx="7" cy="7" r="6" fill="none" stroke="#fff" stroke-width="1.3"/><path d="M4.6 4c.4-.4.8-.3 1 .1l.6 1.1c.2.3 0 .6-.2.8l-.3.3c.4.9 1.1 1.6 2 2l.3-.3c.2-.2.5-.4.8-.2l1.1.6c.4.2.5.6.1 1-.8.8-2 .9-3.4-.1-1.1-.8-2-1.7-2.6-2.8-.6-1.2-.3-2 .6-2.5z" fill="#fff"/></svg>
        (555) 014-2290
      </span>
      <span class="contact-item">
        <svg viewBox="0 0 14 14" fill="none" stroke="#fff" stroke-width="1.1"><circle cx="7" cy="7" r="6"/><ellipse cx="7" cy="7" rx="2.6" ry="6"/><path d="M1 7h12M2 4h10M2 10h10"/></svg>
        harborglowacupuncture.com
      </span>
    </footer>
  </main>
</body>
</html>
```